Veltrona Web Presence

I need a word press site for my company that houses diverse services, and am looking to profile these areas: Design and Delivery of Social Innovation Initiatives, Innovative Pubic Engagement, The Turquoise Economy, Youth Entrepreneurship, and The Science of Change.

I would also like to profile my recent projects. A blog, video and photos are also important features.

Industry/Entity Type

It Company

Requirements
Must have
• I would like to have an overview of what the company does as a Think, Feel and Do Company, along with sections for specific services and recent project profiles.

I would like a section for a blog

I would like a section for photos and video.

I would like the look and feel of the website to reflect the following:

Marisol has spent 30 years leading expeditions into the future. Marisol has a special interest in exploring the changing business, social and cultural landscapes and frontiers, uncovering uncharted territory and unleashing hidden potential – within the person, family, organization, community, business or marketplace. Marisol thrives on experimentation that has led to blended eastern and western methodologies and technologies that help people and organizations deal with the chronic and tough issues in research-based, intelligent and inspiring ways.

Specialties:Breaking down the walls between disciplines such as environmental, social, and economic approaches to create ideologies and methodologies that weave them all to change the way we live. This ideology and methodology applies to all areas: business development, business identity, strategy for all organizations - public, private and NGO.This starts at the individual level.Marisol is also an energy healer specializing in belief reconstruction leading to fulfilling lives.

```html
<!DOCTYPE html>
<html lang="en">
<head>
<meta charset="utf-8">
<title>Veltrona — Social Innovation Initiatives</title>
<link rel="stylesheet" href="https://fonts.googleapis.com/css2?family=Source+Sans+3:wght@300;400;600&family=PT+Sans+Narrow:wght@700&display=swap">
<style>
  :root {
    --brand-blue: #1d5ba8;
    --heading-blue: #2a64b2;
    --coral: #f0625a;
    --orange: #f29a1c;
    --lime: #8dbf22;
    --text-dark: #2b2b2b;
    --text-muted: #8e8e8e;
    --rule: #e2e2e2;
    --footer-bg: #1b2c49;
    --footer-text: #c9d1de;
    --white: #ffffff;
  }
  * { margin: 0; padding: 0; box-sizing: border-box; }
  html, body { width: 1065px; height: 1200px; overflow: hidden; background: var(--white); }
  body { position: relative; font-family: "Source Sans 3", Arial, sans-serif; color: var(--text-dark); }

  /* Header */
  .site-header { position: absolute; top: 0; left: 0; width: 1065px; height: 120px; }
  .brand { position: absolute; left: 56px; top: 28px; font-size: 54px; font-weight: 400; color: var(--brand-blue); letter-spacing: 0.5px; line-height: 1; }
  .main-nav { position: absolute; right: 48px; top: 70px; display: flex; }
  .main-nav a { font-size: 18px; color: var(--brand-blue); text-decoration: none; padding: 0 18px; line-height: 24px; border-left: 1px solid #cfd6e2; }
  .main-nav a:first-child { border-left: none; }
  .main-nav a:last-child { padding-right: 0; }

  /* Hero */
  .hero { position: absolute; top: 120px; left: 0; width: 1065px; height: 448px; overflow: hidden; }
  .hero-photo { position: absolute; inset: 0;
    background: linear-gradient(100deg, #7a6a4d 0%, #8fa35a 22%, #a9c46a 45%, #7f9a52 65%, #5c6b48 85%, #3e4a36 100%); }
  .hero-photo::after { content: ""; position: absolute; inset: 0;
    background: linear-gradient(180deg, rgba(190,220,140,0.35) 0%, rgba(60,60,50,0.25) 70%, rgba(40,40,35,0.4) 100%); }
  .hero-title { position: absolute; left: 0; top: 0; font-family: "PT Sans Narrow", "Arial Narrow", sans-serif; font-weight: 700; color: var(--white); text-transform: uppercase; line-height: 1; }
  .hero-title span { position: absolute; white-space: nowrap; }
  .hero-title .line-1 { left: 99px; top: 176px; font-size: 50px; }
  .hero-title .line-2 { left: 130px; top: 215px; font-size: 82px; }
  .hero-title .line-3 { left: 199px; top: 290px; font-size: 46px; }
  .hero-arrows { position: absolute; left: 972px; top: 398px; }

  /* Intro */
  .intro { position: absolute; top: 602px; left: 0; width: 1065px; text-align: center; }
  .intro h1 { font-size: 34px; font-weight: 400; color: var(--coral); line-height: 42px; }
  .intro p { width: 840px; margin: 6px auto 0; font-size: 15px; font-weight: 300; color: var(--text-muted); line-height: 21px; }
  .divider { position: absolute; top: 723px; left: 66px; width: 948px; border-top: 1px solid var(--rule); }

  /* Columns */
  .column { position: absolute; top: 776px; }
  .column h2 { font-size: 24px; font-weight: 400; line-height: 32px; }
  .blog { left: 56px; width: 300px; }
  .blog h2 { color: var(--heading-blue); }
  .blog-post { position: absolute; left: 1px; width: 300px; }
  .blog-post h3 { font-size: 14.5px; font-weight: 400; color: var(--text-dark); line-height: 20px; }
  .blog-post p { margin-top: 3px; font-size: 12.5px; font-weight: 300; color: var(--text-muted); line-height: 21px; }
  .post-1 { top: 47px; }
  .post-2 { top: 132px; }
  .post-3 { top: 210px; }

  .video { left: 379px; width: 330px; }
  .video h2 { color: var(--orange); top: 2px; position: relative; }
  .video-frame { position: absolute; top: 40px; left: 1px; width: 327px; height: 221px; border: 1px solid #dcdcdc;
    background: radial-gradient(ellipse at 50% 45%, #f3e3bf 0%, #e9c27a 28%, #f2f2f2 60%, #ffffff 100%); }
  .play-button { position: absolute; left: 143px; top: 90px; }

  .gallery { left: 742px; width: 290px; }
  .gallery h2 { color: var(--lime); }
  .thumbs { position: absolute; top: 39px; left: 1px; display: grid; grid-template-columns: repeat(3, 81px); grid-auto-rows: 67px; column-gap: 10px; row-gap: 9px; }
  .thumb { display: block; }
  .t1 { background: linear-gradient(160deg, #d9e7f0, #c98b55); }
  .t2 { background: linear-gradient(160deg, #bcd5dc, #7d9a8a); }
  .t3 { background: linear-gradient(160deg, #a9c37b, #e3c7a6); }
  .t4 { background: linear-gradient(160deg, #e6e9ec, #3d4048); }
  .t5 { background: linear-gradient(160deg, #e9f3f7, #9fc6d8); }
  .t6 { background: linear-gradient(160deg, #3d5b78, #c99a7c); }
  .t7 { background: linear-gradient(160deg, #c9d4dd, #8a6a50); }
  .t8 { background: linear-gradient(160deg, #6f8bb3, #2d2a2a); }
  .t9 { background: linear-gradient(160deg, #c4d69a, #6d4a37); }

  /* Footer */
  .site-footer { position: absolute; top: 1113px; left: 0; width: 1065px; height: 87px; background: var(--footer-bg); }
  .copyright { position: absolute; left: 61px; top: 32px; font-size: 12.5px; font-weight: 300; color: var(--footer-text); }
  .social { position: absolute; left: 866px; top: 20px; display: flex; gap: 4px; }
  .social span { width: 30px; height: 30px; border-radius: 50%; background: var(--white); display: block; }
</style>
</head>
<body>
  <header class="site-header">
    <div class="brand">Veltrona</div>
    <nav class="main-nav">
      <a href="#">HOME</a>
      <a href="#">ABOUT US</a>
      <a href="#">VIDEO</a>
      <a href="#">BLOG</a>
      <a href="#">CONTACT US</a>
    </nav>
  </header>

  <section class="hero">
    <div class="hero-photo" role="img" aria-label="Photo of a group of young people talking together outdoors on a sunny campus lawn"></div>
    <h2 class="hero-title">
      <span class="line-1">Social</span>
      <span class="line-2">Innovation</span>
      <span class="line-3">Initiatives</span>
    </h2>
    <svg class="hero-arrows" width="36" height="24" viewBox="0 0 36 24" aria-hidden="true">
      <polyline points="12,3 4,12 12,21" fill="none" stroke="#ffffff" stroke-width="2.5"/>
      <polyline points="24,3 32,12 24,21" fill="none" stroke="#ffffff" stroke-width="2.5"/>
    </svg>
  </section>

  <section class="intro">
    <h1>Nunc tempus felis vitae urna</h1>
    <p>Phasellus felis dolor, scelerisque a, tempus eget, lobortis id, libero. Donec scelerisque leo ac risus. Praesent sit amet est. In dictum, dolor eu dictum porttitor, enim felis viverra mi, eget luctus massa purus quis odio.</p>
  </section>
  <div class="divider"></div>

  <section class="column blog">
    <h2>Recent Blog</h2>
    <article class="blog-post post-1">
      <h3>Duis sed tellus et tortor vestibulum gravida</h3>
      <p>Duis sed tellus et tortor vestibulum gravida. Praesent elementum elit at tellus. Curabitur metus ipsum</p>
    </article>
    <article class="blog-post post-2">
      <h3>Vivamus porttitor g purus</h3>
      <p>Maecenas aliquet velit vel turpis. Mauris neque metus, malesuada nec, ultricies sit amet</p>
    </article>
    <article class="blog-post post-3">
      <h3>Class aptent taciti sociosqu</h3>
      <p>Maecenas aliquet velit vel turpis. Mauris neque metus, malesuada nec, ultricies sit amet</p>
    </article>
  </section>

  <section class="column video">
    <h2>Watch Our Video</h2>
    <div class="video-frame" role="img" aria-label="Video still: illustration of figures holding hands in a circle around a light bulb">
      <svg class="play-button" width="40" height="40" viewBox="0 0 40 40" aria-hidden="true">
        <circle cx="20" cy="20" r="19" fill="#ffffff"/>
        <circle cx="20" cy="20" r="16" fill="#1e1e1e"/>
        <polygon points="16,12 28,20 16,28" fill="#ffffff"/>
      </svg>
    </div>
  </section>

  <section class="column gallery">
    <h2>Photo Gallery</h2>
    <div class="thumbs">
      <span class="thumb t1" role="img" aria-label="Photo of friends with raised arms outdoors"></span>
      <span class="thumb t2" role="img" aria-label="Photo of a businessman under a floating cube"></span>
      <span class="thumb t3" role="img" aria-label="Photo of a smiling older couple"></span>
      <span class="thumb t4" role="img" aria-label="Photo of a business team"></span>
      <span class="thumb t5" role="img" aria-label="Photo of a light bulb over a landscape"></span>
      <span class="thumb t6" role="img" aria-label="Portrait photo of a young man"></span>
      <span class="thumb t7" role="img" aria-label="Photo of colleagues in a meeting"></span>
      <span class="thumb t8" role="img" aria-label="Photo of a businessman at an office desk"></span>
      <span class="thumb t9" role="img" aria-label="Portrait photo of a smiling child"></span>
    </div>
  </section>

  <footer class="site-footer">
    <p class="copyright">© 2013 Company Name.&nbsp; All right reserved.&nbsp; Term of Use</p>
    <div class="social" aria-label="Social links">
      <span></span><span></span><span></span><span></span>
    </div>
  </footer>
</body>
</html>
```